Book cover for ebook and Physical book for Mind Clutter Collective

I run a non-profit Mind Clutter Collective and I have a new book that needs a cover. For the physical book, I will need a full wrap. The mission is to help individuals Quiet the cycle of restless worry patterns. This book is title is "Quiet the cycle of restless worry patterns", and subtitle "Clear Your Mind of Static Noise." I am open to anything design wise, nothing is set in stone. Oh, MCC is pending Trademark.

Target Market(s)

Typically it's Mom's from 25-40

Industry/Entity Type

Mental Health

Font styles to use
Serif

Colors
f37122
9bcb3b
fbed22
0255a3
e34197

Requirements
Must have
• I do like simplicity, yet vibrant colors.
Nice to have
• The authors are Rex T. Whitford, and Dana Okonkwo. For some inspiration individuals refer to me as the Wonder Guide having reversed five incurable diseases.
Should not have
• The cover shouldn't be too busy.

```html
<!DOCTYPE html>
<html lang="en">
<head>
<meta charset="utf-8">
<title>Quiet the cycle of restless worry patterns — Book Cover</title>
<link rel="stylesheet" href="https://fonts.googleapis.com/css2?family=PT+Serif:ital,wght@0,400;1,700&family=PT+Sans:wght@400&display=swap">
<style>
  :root {
    --page-bg: #ffffff;
    --brand-blue: #0255a3;
    --blue-facet: rgba(255, 255, 255, 0.07);
    --subtitle-tint: rgba(120, 170, 225, 0.45);
    --body-blue: #0b4d9e;
    --accent-green: #9bcb3b;
    --accent-bar: #6aa8e0;
    --credit-panel: rgba(255, 255, 255, 0.45);
    --photo-light: #eee9d6;
    --photo-warm: #d2c6ae;
    --white: #ffffff;
  }

  html, body {
    margin: 0;
    width: 1200px;
    height: 1000px;
    overflow: hidden;
    background: var(--page-bg);
  }

  .canvas {
    position: relative;
    width: 1200px;
    height: 1000px;
  }

  .book-cover {
    position: absolute;
    left: 258px;
    top: 3px;
    width: 684px;
    height: 985px;
    overflow: hidden;
    box-shadow: 0 8px 4px -2px rgba(0, 0, 0, 0.55), 0 0 0 1px rgba(0, 0, 0, 0.25);
  }

  .cover-photo {
    position: absolute;
    inset: 0;
    background: linear-gradient(180deg, var(--photo-light) 0%, var(--photo-warm) 100%);
  }

  .header-band {
    position: absolute;
    left: 0;
    top: 0;
  }

  .title {
    position: absolute;
    left: 20px;
    top: 14px;
    width: 320px;
    margin: 0;
    text-align: center;
    font-family: "PT Serif", serif;
    font-style: italic;
    font-weight: 700;
    font-size: 32px;
    line-height: 42px;
    color: var(--white);
  }

  .subtitle {
    position: absolute;
    left: 17px;
    top: 192px;
    width: 325px;
    height: 29px;
    margin: 0;
    background: var(--subtitle-tint);
    text-align: center;
    font-family: "PT Serif", serif;
    font-weight: 400;
    font-size: 19px;
    line-height: 29px;
    color: var(--white);
  }

  .blurb {
    position: absolute;
    left: 241px;
    top: 316px;
    width: 430px;
    margin: 0;
    font-family: "PT Sans", sans-serif;
    font-size: 20px;
    letter-spacing: 0.5px;
    line-height: 27.3px;
    color: var(--body-blue);
    white-space: nowrap;
  }

  .highlight-box {
    position: absolute;
    left: 60px;
    top: 633px;
    width: 599px;
    height: 89px;
    background: var(--accent-green);
  }

  .highlight-text {
    position: absolute;
    left: 22px;
    top: 19px;
    margin: 0;
    font-family: "PT Sans", sans-serif;
    font-size: 18px;
    letter-spacing: 0.2px;
    line-height: 25px;
    color: var(--white);
    white-space: nowrap;
  }

  .authors {
    position: absolute;
    left: 391px;
    top: 822px;
    width: 293px;
    height: 86px;
    background: var(--credit-panel);
  }

  .authors-bar {
    position: absolute;
    left: 19px;
    top: 14px;
    width: 9px;
    height: 59px;
    background: var(--accent-bar);
  }

  .authors-names {
    position: absolute;
    right: 25px;
    top: 10px;
    margin: 0;
    text-align: right;
    font-family: "PT Serif", serif;
    font-weight: 400;
    font-size: 28px;
    line-height: 36px;
    color: var(--brand-blue);
    white-space: nowrap;
  }
</style>
</head>
<body>
<div class="canvas">
  <div class="book-cover">
    <div class="cover-photo" role="img" aria-label="Cover photograph: a person meditating on a wooden dock beside a calm lake"></div>

    <svg class="header-band" width="684" height="245" viewBox="0 0 684 245" aria-hidden="true">
      <polygon points="0,0 684,0 684,89 428,89 353,240 0,240" fill="var(--brand-blue)"/>
      <polygon points="70,0 445,0 312,142" fill="var(--blue-facet)"/>
      <polyline points="684,89 428,89 353,240 0,240" fill="none" stroke="var(--white)" stroke-width="4"/>
    </svg>

    <h1 class="title">Quiet the cycle<br>of restless<br>worry<br>patterns</h1>
    <p class="subtitle">Clear Your Mind of Static Noise</p>

    <p class="blurb">Lorem ipsum dolor sit amet, quo et mazim in<br>ix ei idque intellegat referrentur. Suas deterr<br>uri disputando ex usu. Justo epicurei tacimat<br>atqui quaestio vis. Summo errem et qui, nihil<br>s id, ut efficiantur intellegebat sit.Usu platon<br>ix ei idque intellegat referrentur. Suas deterr<br>uri disputando ex usu. Justo epicurei tacimat<br>atqui quaestio vis. Summo errem et qui, nihil<br>s id, ut efficiantur intellegebat sit.Usu platon<br>uri disputando ex usu. Justo epi</p>

    <div class="highlight-box">
      <p class="highlight-text">Lorem ipsum dolor sit amet, quo et mazim in uri disputando ex u<br>ix ei idque intellegat referrentur. Suas deterr atqui quaestio</p>
    </div>

    <div class="authors">
      <div class="authors-bar"></div>
      <p class="authors-names">Rex T. Whitford &amp;<br>Dana Okonkwo</p>
    </div>
  </div>
</div>
</body>
</html>
```